BRISKWAY traffic management plans

The preparation of traffic management plans for architects, builders, landscapers for council approval. The preparation of the plans can include submitting to council, briefing the builder regarding management of the plan, onsite visit, taking photographs, measurements and establishing the best outcome. Implementing the plan can also take place if need be.
NO EXISTING LOGO AVAILABLE
No photos or documents available to upload

Target Market(s)

Builders, architects, landscapers
No existing logo availalble

Industry/Entity Type

Builders

Contact Information for Business Card

BRISKWAY Traffic Management Plans
Tom Brindley
harbourlane@zentrynet.com.au
0427 693 058

Font styles to use
Serif

Colors
1b1b1b

Requirements
Must have
• competitive prices
• No existing logo available
• No photos available
Nice to have
• Black with orange and white
• No existing logo available no
Should not have
• no existing logo available
• No photos or documents to upload

```html
<!DOCTYPE html>
<html lang="en">
<head>
<meta charset="utf-8">
<title>BRISKWAY Traffic Management Plans – Business Cards</title>
<link rel="stylesheet" href="https://fonts.googleapis.com/css2?family=Open+Sans:wght@400;600;700;800&display=swap">
<style>
  :root {
    --orange: #d64400;
    --orange-bright: #e85200;
    --black: #1b1b1b;
    --white: #ffffff;
    --backdrop: #ece9e6;
  }
  * { box-sizing: border-box; margin: 0; padding: 0; }
  html, body { width: 1200px; height: 900px; overflow: hidden; }
  body {
    background: var(--backdrop);
    font-family: "Open Sans", Arial, sans-serif;
    position: relative;
  }
  .card {
    position: absolute;
    overflow: hidden;
    box-shadow: 0 6px 18px rgba(0,0,0,0.18);
  }
  .card-front {
    left: 78px; top: 34px; width: 587px; height: 363px;
    background: var(--white);
  }
  .card-front .bands { position: absolute; inset: 0; }
  .brand {
    position: absolute;
    display: flex; align-items: center; gap: 14px;
  }
  .brand-square { width: 26px; height: 26px; }
  .brand-text { font-weight: 800; line-height: 1; }
  .brand-name { letter-spacing: 1px; }
  .brand-tagline { letter-spacing: 0.2px; margin-top: 6px; }

  .card-front .brand { left: 112px; top: 82px; color: var(--orange); }
  .card-front .brand-square { background: var(--orange); }
  .card-front .brand-name { font-size: 62px; }
  .card-front .brand-tagline { font-size: 17px; }

  .contact {
    position: absolute; left: 0; right: 0; top: 232px;
    text-align: center; color: var(--white);
  }
  .contact-name { font-size: 23px; font-weight: 700; letter-spacing: 0.3px; }
  .contact-line { font-size: 17px; font-weight: 400; line-height: 22px; }
  .contact-name + .contact-line { margin-top: 22px; }

  .card-back {
    left: 388px; top: 505px; width: 566px; height: 352px;
    background: linear-gradient(180deg, var(--orange-bright), var(--orange));
  }
  .card-back .brand { left: 110px; top: 130px; color: var(--white); }
  .card-back .brand-square { background: var(--white); }
  .card-back .brand-name { font-size: 62px; }
  .card-back .brand-tagline { font-size: 17px; }
</style>
</head>
<body>
  <section class="card card-front" aria-label="Business card front">
    <svg class="bands" width="587" height="363" viewBox="0 0 587 363" aria-hidden="true">
      <polygon points="0,199 402,199 382,226 0,226" fill="var(--black)"/>
      <polygon points="0,230 386,230 413,192 587,192 587,363 0,363" fill="var(--orange)"/>
    </svg>
    <div class="brand">
      <span class="brand-square"></span>
      <div class="brand-text">
        <div class="brand-name">BRISKWAY</div>
        <div class="brand-tagline">Traffic Management Plans</div>
      </div>
    </div>
    <div class="contact">
      <p class="contact-name">TOM BRINDLEY</p>
      <p class="contact-line">0427 693 058</p>
      <p class="contact-line">harbourlane@zentrynet.com.au</p>
    </div>
  </section>

  <section class="card card-back" aria-label="Business card back">
    <div class="brand">
      <span class="brand-square"></span>
      <div class="brand-text">
        <div class="brand-name">BRISKWAY</div>
        <div class="brand-tagline">Traffic Management Plans</div>
      </div>
    </div>
  </section>
</body>
</html>
```